We need a flyer where we promote a workshop to our members of the jewish community www.qvb-gemeinde.example . The workshop is calles "guidance in ten seasons presented by QVB. We would like to see a flyer with the below text is used and also some pictures (attached). The flyer should come over as cool, fresh, innovative for a younger crowd so called young professionals (age 28-35).
TITLE.
"Guidance in Ten Seasons.
SUBTITLE.
Your systematic self-coaching roadmap to power and impact—and your future.”
TEXT.
Dr. Martin K. Halvorsen is the CEO Emeritus of Alpine Advisory Partners—he made an exit in 2013. He is the award-winning author of 8 books, including "Plan-Into-Motion," "Speak or Falter" and "The Cantor and the Chairman.”
For the past 20 years he has taught leadership at Harwick University in New York and at BKU (Lindenberg University) to prepare future CEOs and other leaders in business, government , nonprofits and the military.
Now, in a process exclusively designed for QVB’s next generation of emerging leaders, Martin unpacks his leadership secrets in 3 action-packed labs—reduced to the max:
Lab 1. Guidance in Ten Seasons: The Summit Guide Triangle®. Self-Assessment. Self-Leadership: “The Lantern.” 5-Year Vision. 100-Day Catalytic Project.
Lab 2. Leading Through Language. Relationship: Building Trust. Plan-Into-Motion. Cockpit.
Lab 3. Debrief and Scale-Up. Sustainability. Action Tools.
Do you want to build your own future and a life you love? Do you want to jump-start that future and life over 100 days while learning a toolbox of leadership skills, networking with like-minded people—and even get some pizza? Then join us.
Target Market(s)
young professionals age 28-35

```html
<!DOCTYPE html>
<html lang="en">
<head>
<meta charset="utf-8">
<title>Guidance in Ten Seasons — Workshop Flyer</title>
<link href="https://fonts.googleapis.com/css2?family=Bebas+Neue&family=Oswald:wght@600&family=Figtree:wght@500;600;700&display=swap" rel="stylesheet">
<style>
  :root {
    --backdrop: #7b7b7b;
    --flyer-red: #c3120f;
    --ink-black: #050505;
    --headline-yellow: #f3cf6a;
    --text-white: #ffffff;
    --lab-red: #b3110e;
    --lab-box: #ececec;
  }
  * { margin: 0; padding: 0; box-sizing: border-box; }
  html, body {
    width: 1200px; height: 904px; overflow: hidden;
    background: var(--backdrop);
  }
  .flyer {
    position: absolute; left: 330px; top: 21px;
    width: 540px; height: 862px;
    background: var(--flyer-red);
    overflow: hidden;
    font-family: "Figtree", Arial, sans-serif;
    color: var(--text-white);
  }
  .flyer-header {
    position: absolute; left: 0; top: 0; width: 100%; height: 96px;
    display: flex; align-items: center; justify-content: center;
    text-align: center;
    color: var(--headline-yellow);
    font-weight: 700; font-size: 21px; line-height: 30px;
    padding: 0 20px;
  }
  .title-band {
    position: absolute; left: 0; top: 96px; width: 100%; height: 300px;
    background:
      radial-gradient(ellipse at 65% 55%, rgba(200,20,20,0.75), rgba(80,5,5,0.6) 45%, transparent 75%),
      linear-gradient(180deg, #1a0303 0%, #3a0606 55%, #140202 100%);
  }
  .title {
    position: absolute; left: 0; top: 96px; width: 100%; height: 300px;
    display: flex; flex-direction: column; align-items: center; justify-content: center;
    font-family: "Bebas Neue", Impact, sans-serif;
    font-weight: 400;
    color: var(--text-white);
    line-height: 0.86;
    text-align: center;
  }
  .title-line-1 { font-size: 116px; letter-spacing: 2px; }
  .title-line-2 { font-size: 52px; margin: 4px 0 2px; }
  .title-line-3 { font-size: 92px; letter-spacing: 1px; }
  .bio {
    position: absolute; left: 26px; top: 412px; width: 488px;
    font-size: 12px; line-height: 16px; font-weight: 500;
    text-align: justify;
  }
  .bio p + p { margin-top: 9px; }
  .intro {
    position: absolute; left: 26px; top: 544px; width: 360px;
    color: var(--headline-yellow);
    font-size: 11px; line-height: 15px; font-weight: 700;
    white-space: nowrap;
  }
  .labs {
    position: absolute; left: 26px; top: 600px; width: 350px;
    list-style: none;
    display: flex; flex-direction: column; gap: 13px;
  }
  .lab { display: flex; align-items: center; }
  .lab-tag {
    position: relative; width: 50px; height: 34px; flex: none;
    background: var(--lab-box);
    color: var(--lab-red);
    font-family: "Oswald", "Arial Narrow", sans-serif; font-weight: 600;
    font-size: 17px; line-height: 34px; text-align: center; letter-spacing: -0.3px;
  }
  .lab-tag::after {
    content: ""; position: absolute; right: -5px; top: 12px;
    border-left: 5px solid var(--lab-box);
    border-top: 5px solid transparent; border-bottom: 5px solid transparent;
  }
  .lab-text {
    margin-left: 12px; font-size: 10.2px; line-height: 14px; font-weight: 500;
    white-space: nowrap;
  }
  .footer-band {
    position: absolute; left: 0; top: 803px; width: 100%; height: 59px;
    background: var(--ink-black);
  }
  .footer-band { top: 803px; }
  .footer-band.main { top: 803px; }
  .footer-panel {
    position: absolute; left: 0; top: 803px; width: 100%; height: 59px;
  }
  .invitation-band {
    position: absolute; left: 0; top: 745px; width: 100%; height: 117px;
    background: var(--ink-black);
  }
  .invitation {
    position: absolute; left: 26px; top: 755px; width: 300px;
    font-size: 10px; line-height: 13.5px; font-weight: 500;
    white-space: nowrap;
  }
  .brand {
    position: absolute; left: 178px; top: 826px;
    color: var(--headline-yellow);
    font-size: 13px; font-weight: 600; letter-spacing: 0.5px;
    display: flex; align-items: center; gap: 6px;
  }
  .brand-dot { width: 9px; height: 9px; border-radius: 50%; background: var(--headline-yellow); }
  .speaker-portrait {
    position: absolute; left: 325px; top: 526px; width: 215px; height: 336px;
  }
</style>
</head>
<body>
  <main class="flyer">
    <header class="flyer-header">Your Systematic Self-Coaching Roadmap to Power and Impact—and Your Future.</header>

    <div class="title-band" role="img" aria-label="Photo of a speaker on stage in front of a large audience, tinted red"></div>
    <h1 class="title">
      <span class="title-line-1">GUIDANCE</span>
      <span class="title-line-2">IN</span>
      <span class="title-line-3">TEN SEASONS</span>
    </h1>

    <section class="bio">
      <p>Dr. Martin K. Halvorsen is the CEO Emeritus of Alpine Advisory Partners—he made an exit in 2013. He is the award-winning author of 8 books, including "Plan-Into-Motion," "Speak or Falter" and "The Cantor and the Chairman.”</p>
      <p>For the past 20 years he has taught leadership at Harwick University in New York and at BKU (Lindenberg University) to prepare future CEOs and other leaders in business, government , nonprofits and the military.</p>
    </section>

    <p class="intro">Now, in a process exclusively designed for QVB’s next generation<br>of emerging leaders, Martin unpacks his leadership secrets in<br>3 action-packed labs—reduced to the max:</p>

    <ul class="labs">
      <li class="lab"><span class="lab-tag">Lab 1.</span><span class="lab-text">Guidance in Ten Seasons: The Summit Guide Triangle®.<br>Self-Assessment. Self-Leadership:<br>“The Lantern.” 5-Year Vision. 100-Day Catalytic Project.</span></li>
      <li class="lab"><span class="lab-tag">Lab 2.</span><span class="lab-text">Leading Through Language. Relationship:<br>Building Trust. Plan-Into-Motion. Cockpit.</span></li>
      <li class="lab"><span class="lab-tag">Lab 3.</span><span class="lab-text">Debrief and Scale-Up. Sustainability.<br>Action Tools.</span></li>
    </ul>

    <div class="invitation-band"></div>
    <p class="invitation">Do you want to build your own future and a life you love?<br>Do you want to jump-start that future and life over<br>100 days while learning a toolbox of leadership skills,<br>networking with like-minded people—<br>and even get some pizza?<br>Then join us.</p>

    <div class="brand"><span class="brand-dot"></span>Nordlicht Labs</div>

    <svg class="speaker-portrait" role="img" aria-label="Portrait photo of the speaker in a grey suit with arms crossed" viewBox="0 0 215 336" preserveAspectRatio="none">
      <defs>
        <linearGradient id="portrait-tone" x1="0" y1="0" x2="0" y2="1">
          <stop offset="0" stop-color="#c3120f" stop-opacity="0"/>
          <stop offset="0.35" stop-color="#6b6a6e"/>
          <stop offset="1" stop-color="#3e3e44"/>
        </linearGradient>
      </defs>
      <path d="M75 0 H155 V120 L215 150 V336 H30 V200 L75 150 Z" fill="url(#portrait-tone)"/>
    </svg>
  </main>
</body>
</html>
```